Brivolands Vehicle Wrap Design for Vacation Rental Property Mgt Company

We are looking for a vehicle wrap design to extend our brand through our service vehicles. Design should be simple, professional, eye-catching, and incorporate our logo and corporate colors. Design should be flexible enough to be applied to a wide variety of trucks and cars. Not looking for FULL wrap, but rather separate graphics to be applied to white vehicles. Attached is ppt with a couple of our current vehicles and a few sample designs that has caught our attention. Copies of our current logo and biz card designs are also included.

Panels to include:
Logo (attached)
555-384-9126
www.Brivolands.example
Vacation Rental Property Management
Property Maintenance Services
Linen & Laundry Services

Target Market(s)

Local adults 30-65

Industry/Entity Type

Font styles to use
Serif

Colors
0054AA
0677BA
7BADD7
CADEEF
E8F1F8

Requirements
Must have
• Logo, phone, web address, corporate colors,

```html
<!DOCTYPE html>
<html lang="en">
<head>
<meta charset="utf-8">
<title>Brivolands Vehicle Wrap Graphics</title>
<link href="https://fonts.googleapis.com/css2?family=Oswald:wght@500&family=Roboto+Condensed:ital,wght@0,500;0,600;1,500&family=Montserrat:wght@600&display=swap" rel="stylesheet">
<style>
  :root {
    --navy: #0b3a78;
    --brand-blue: #0054AA;
    --mid-blue: #0677BA;
    --sky-blue: #2a9ad8;
    --pale-blue: #CADEEF;
    --white: #ffffff;
    --canvas-bg: #ffffff;
  }
  * { margin: 0; padding: 0; box-sizing: border-box; }
  html, body {
    width: 1200px;
    height: 627px;
    overflow: hidden;
    background: var(--canvas-bg);
  }
  .wrap-design {
    position: relative;
    width: 1200px;
    height: 627px;
    background: var(--white);
    overflow: hidden;
  }
  .wave-graphics {
    position: absolute;
    inset: 0;
    width: 1200px;
    height: 627px;
  }
  .brand-lockup {
    position: absolute;
    left: 0;
    right: 0;
    top: 95px;
    display: flex;
    align-items: center;
    justify-content: center;
    gap: 26px;
  }
  .brand-mark-square {
    width: 84px;
    height: 84px;
    background: var(--navy);
  }
  .brand-text { text-align: center; }
  .brand-name {
    font-family: "Oswald", sans-serif;
    font-weight: 500;
    font-size: 88px;
    line-height: 1;
    letter-spacing: 1px;
    color: var(--navy);
  }
  .brand-tagline {
    margin-top: 10px;
    font-family: "Montserrat", sans-serif;
    font-weight: 600;
    font-size: 22px;
    letter-spacing: 1px;
    color: var(--navy);
  }
  .service-line {
    font-family: "Roboto Condensed", sans-serif;
    font-style: italic;
    font-weight: 500;
    font-size: 19px;
    letter-spacing: 0.4px;
    fill: var(--brand-blue);
  }
  .service-bullet { fill: var(--sky-blue); font-style: normal; }
  .web-address {
    position: absolute;
    left: 878px;
    top: 362px;
    display: flex;
    align-items: center;
    gap: 10px;
    font-family: "Roboto Condensed", sans-serif;
    font-weight: 500;
    font-size: 21px;
    letter-spacing: 1px;
    color: var(--white);
  }
  .phone-number {
    position: absolute;
    left: 650px;
    top: 420px;
    display: flex;
    align-items: center;
    gap: 10px;
    font-family: "Roboto Condensed", sans-serif;
    font-weight: 600;
    font-size: 40px;
    color: var(--white);
  }
  .contact-icon { display: block; }
</style>
</head>
<body>
  <main class="wrap-design">
    <svg class="wave-graphics" viewBox="0 0 1200 627" aria-hidden="true">
      <defs>
        <linearGradient id="bandGradient" x1="0" y1="0" x2="1" y2="0">
          <stop offset="0" stop-color="#0d3a7a"/>
          <stop offset="0.55" stop-color="#0a4a94"/>
          <stop offset="1" stop-color="#1f8fd6"/>
        </linearGradient>
        <path id="serviceCurve" d="M30,428 C430,414 820,334 1185,286"/>
      </defs>
      <path class="wave-band" d="M0,440 C400,432 800,352 1200,300 L1200,627 L0,627 Z" fill="url(#bandGradient)"/>
      <text class="service-line">
        <textPath href="#serviceCurve" startOffset="0">
          <tspan class="service-bullet">● </tspan>VACATION RENTAL PROPERTY MANAGEMENT
          <tspan class="service-bullet"> ● </tspan>PROPERTY MAINTENANCE SERVICES
          <tspan class="service-bullet"> ● </tspan>LINEN &amp; LAUNDRY SERVICES
        </textPath>
      </text>
    </svg>

    <header class="brand-lockup">
      <div class="brand-mark-square"></div>
      <div class="brand-text">
        <h1 class="brand-name">BRIVOLANDS</h1>
        <p class="brand-tagline">VACATION RENTALS</p>
      </div>
    </header>

    <div class="web-address">
      <svg class="contact-icon" width="26" height="26" viewBox="0 0 26 26" aria-hidden="true">
        <g fill="none" stroke="#7BADD7" stroke-width="1.8">
          <circle cx="13" cy="13" r="11"/>
          <ellipse cx="13" cy="13" rx="5" ry="11"/>
          <line x1="2" y1="13" x2="24" y2="13"/>
          <path d="M4,7 H22 M4,19 H22"/>
        </g>
      </svg>
      <span>www.Brivolands.example</span>
    </div>

    <div class="phone-number">
      <svg class="contact-icon" width="30" height="30" viewBox="0 0 24 24" aria-hidden="true">
        <path fill="#7BADD7" d="M6.6 10.8a15.1 15.1 0 0 0 6.6 6.6l2.2-2.2a1 1 0 0 1 1-.25 11.4 11.4 0 0 0 3.6.57 1 1 0 0 1 1 1V20a1 1 0 0 1-1 1A17 17 0 0 1 3 4a1 1 0 0 1 1-1h3.5a1 1 0 0 1 1 1c0 1.25.2 2.45.57 3.57a1 1 0 0 1-.25 1z"/>
      </svg>
      <span>555-384-9126</span>
    </div>
  </main>
</body>
</html>
```